design cheese package for ORVEN

We want someone to give me some graphic designs for the cheese package. You shall not only design it on the basis of our product sizes, but also the design with my company Logo shall be novel and attactive. There are some pictures in the attachments: picture 1--3 for my product; picture 4 for my company Logo; picture 5--6 for your reference Thanks! please add the word ORVEN in the package design, thanks!

```html
<!DOCTYPE html>
<html lang="en">
<head>
<meta charset="utf-8">
<title>ORVEN Cheese Packaging</title>
<link href="https://fonts.googleapis.com/css2?family=Cinzel:wght@600;700&family=Archivo:wght@600;800&display=swap" rel="stylesheet">
<style>
  :root {
    --bg: #e9e4dc;
    --cheddar-block: #f3c489;
    --gouda-block: #f2b35c;
    --mozzarella-block: #f1d9b3;
    --olive: #6d7b38;
    --olive-dark: #3f4a1c;
    --gold: #f3b42f;
    --cheddar: #e8343a;
    --gouda: #f38a1e;
    --mozzarella: #3d7cc4;
    --white: #ffffff;
    --ink: #2a2a22;
  }
  * { margin: 0; padding: 0; box-sizing: border-box; }
  html, body { width: 668px; height: 1200px; overflow: hidden; }
  body {
    background: var(--bg);
    position: relative;
    font-family: "Archivo", Arial, sans-serif;
  }
  .package {
    position: absolute;
    left: 129px;
    width: 417px;
    height: 287px;
    border-radius: 14px;
    box-shadow: inset 0 0 0 3px rgba(255,255,255,0.25);
  }
  .package--cheddar { top: 129px; background: var(--cheddar-block); }
  .package--gouda { top: 456px; background: var(--gouda-block); }
  .package--mozzarella { top: 777px; background: var(--mozzarella-block); }

  .label {
    position: absolute;
    left: 67px;
    top: 31px;
    width: 283px;
    height: 225px;
    background: var(--white);
    padding: 6px;
  }
  .label__inner {
    position: relative;
    width: 100%;
    height: 100%;
    overflow: hidden;
  }
  .label__crown {
    position: absolute; left: 0; top: 0; width: 100%; height: 66px;
    background: var(--olive);
  }
  .label__grade {
    position: absolute; left: 0; top: 66px; width: 100%; height: 18px;
    background: var(--gold);
    display: flex; justify-content: space-between; align-items: center;
    padding: 0 52px;
    font-weight: 800; font-size: 10px; letter-spacing: 1px;
    color: var(--olive-dark);
  }
  .label__variety {
    position: absolute; left: 0; top: 84px; width: 100%; height: 100px;
    display: flex; flex-direction: column; align-items: center; justify-content: center;
    padding-bottom: 22px;
    font-family: "Cinzel", Georgia, serif;
    font-weight: 700;
    color: var(--white);
    font-size: 24px;
    line-height: 1.05;
    text-align: center;
  }
  .package--cheddar .label__variety { background: var(--cheddar); }
  .package--gouda .label__variety { background: var(--gouda); }
  .package--mozzarella .label__variety { background: var(--mozzarella); }
  .label__net {
    position: absolute; right: 8px; top: 140px;
    font-size: 7px; font-weight: 600; color: var(--white);
    line-height: 1.25; text-align: left;
  }
  .label__base {
    position: absolute; left: 0; bottom: 0; width: 100%; height: 58px;
  }
  .label__base svg { position: absolute; inset: 0; width: 100%; height: 100%; }
  .label__kind {
    position: absolute; left: 0; bottom: 8px; width: 100%;
    text-align: center;
    font-weight: 800; font-size: 15px; letter-spacing: 1px;
    color: var(--ink);
  }
  .brand-seal {
    position: absolute; left: 50%; top: 10px;
    width: 66px; height: 66px; margin-left: -33px;
    border-radius: 50%;
    background: var(--white);
    border: 3px solid var(--olive-dark);
    display: flex; align-items: center; justify-content: center;
    font-weight: 800; font-size: 13px; letter-spacing: 1px;
    color: var(--olive-dark);
  }
</style>
</head>
<body>

<section class="package package--cheddar">
  <div class="label"><div class="label__inner">
    <div class="label__crown"></div>
    <div class="label__grade"><span>CHOICE</span><span>GRADE</span></div>
    <div class="label__variety"><span>Matured</span><span>Cheddar</span></div>
    <div class="label__net">NET WT<br>8 OZ (226g)</div>
    <div class="label__base">
      <svg viewBox="0 0 271 58" preserveAspectRatio="none"><path d="M0 18 Q135.5 -2 271 18 L271 58 L0 58 Z" fill="#ffffff"/></svg>
      <div class="label__kind">CHEESE</div>
    </div>
    <div class="brand-seal">ORVEN</div>
  </div></div>
</section>

<section class="package package--gouda">
  <div class="label"><div class="label__inner">
    <div class="label__crown"></div>
    <div class="label__grade"><span>CHOICE</span><span>GRADE</span></div>
    <div class="label__variety"><span>Gouda</span></div>
    <div class="label__net">NET WT<br>8 OZ (226g)</div>
    <div class="label__base">
      <svg viewBox="0 0 271 58" preserveAspectRatio="none"><path d="M0 18 Q135.5 -2 271 18 L271 58 L0 58 Z" fill="#ffffff"/></svg>
      <div class="label__kind">CHEESE</div>
    </div>
    <div class="brand-seal">ORVEN</div>
  </div></div>
</section>

<section class="package package--mozzarella">
  <div class="label"><div class="label__inner">
    <div class="label__crown"></div>
    <div class="label__grade"><span>CHOICE</span><span>GRADE</span></div>
    <div class="label__variety"><span>Italian</span><span>Mozzarella</span></div>
    <div class="label__net">NET WT<br>8 OZ (226g)</div>
    <div class="label__base">
      <svg viewBox="0 0 271 58" preserveAspectRatio="none"><path d="M0 18 Q135.5 -2 271 18 L271 58 L0 58 Z" fill="#ffffff"/></svg>
      <div class="label__kind">CHEESE</div>
    </div>
    <div class="brand-seal">ORVEN</div>
  </div></div>
</section>

</body>
</html>
```